I need a business Card Design for my practice , i am clinical herbalist. I am a herbalist specializing in Lyme disease, autism, autoimmune diseases, difficult to cure diseasesDifficult to cure diseases. In my innovative practice i link traditional medicine, herbs with science, immunologu ,pharmacology.

Industry/Entity Type

Business

Contact Information for Business Card

My company name : OSRODEK ZIELNIKA
My name : Piotr Weltak
Name of my profession : Fitoterapeuta
In Polish language Fitoterapeuta is Herbalist .

e-mail: piotrweltak@osrodekzielnika.com
www.osrodek-zielnika.pl
phone : 574 806 215
My company adress : Dąbrowa Sękowska 14 , 38-415 Mielnik
I dont have logo .

Requirements
Nice to have
• My company

```html
<!DOCTYPE html>
<html lang="pl">
<head>
<meta charset="utf-8">
<title>Osrodek Zielnika – business card</title>
<link rel="stylesheet" href="https://fonts.googleapis.com/css2?family=Montserrat:wght@600&family=Open+Sans:wght@400;600&display=swap">
<style>
  :root {
    --stage: #323232;
    --paper: #ffffff;
    --leaf: #6bb12a;
    --bark: #8a4f14;
    --ink: #222222;
  }
  * { margin: 0; padding: 0; box-sizing: border-box; }
  html, body { width: 1200px; height: 900px; overflow: hidden; background: var(--stage); }
  body { position: relative; font-family: "Open Sans", Arial, sans-serif; color: var(--ink); }

  .card { position: absolute; top: 306px; width: 440px; height: 272px; overflow: hidden; }
  .card--front { left: 149px; background: var(--paper); }
  .card--back { left: 608px; background: var(--leaf); color: var(--paper); }

  .name-flag { position: absolute; left: 0; top: 26px; }
  .person { position: absolute; left: 37px; top: 27px; }
  .person__name { font-size: 16px; font-weight: 600; letter-spacing: 0.2px; line-height: 20px; }
  .person__first { color: var(--leaf); }
  .person__last { color: var(--bark); }
  .person__role { font-size: 11.5px; line-height: 16px; }

  .brand { position: absolute; display: flex; align-items: center; gap: 8px;
           font-family: "Montserrat", Arial, sans-serif; font-weight: 600; font-size: 20px; letter-spacing: 0.2px; white-space: nowrap; }
  .brand__dot { width: 12px; height: 12px; border-radius: 50%; background: currentColor; }
  .card--front .brand { color: var(--leaf); right: 24px; top: 134px; }
  .card--back .brand { color: var(--paper); left: 0; right: 0; justify-content: center; top: 127px; }

  .contact { position: absolute; left: 28px; top: 200px; font-size: 12px; line-height: 17px; }
  .contact__row { display: flex; align-items: center; gap: 5px; }
  .contact__icon { width: 10px; height: 10px; fill: var(--leaf); flex: none; }
  .address { position: absolute; right: 26px; top: 199px; font-size: 12px; line-height: 16px; text-align: right; }

  .base-bands { position: absolute; left: 0; bottom: 0; }

  .services { position: absolute; top: 180px; list-style: none; font-size: 12px; line-height: 20px; }
  .services--left { left: 55px; }
  .services--right { left: 272px; top: 181px; }
  .services li { display: flex; align-items: center; gap: 6px; }
  .services li::before { content: ""; width: 6px; height: 6px; border-radius: 50%; background: var(--paper); }
</style>
</head>
<body>

<section class="card card--front" aria-label="Front of business card">
  <svg class="name-flag" width="30" height="38" viewBox="0 0 30 38" aria-hidden="true">
    <polygon points="0,0 12,0 16,38 0,38" fill="var(--bark)"/>
    <polygon points="12,0 28,0 28,38 16,38" fill="var(--leaf)"/>
    <polygon points="11,0 14,0 18,38 15,38" fill="var(--paper)"/>
  </svg>
  <div class="person">
    <p class="person__name"><span class="person__first">PIOTR</span> <span class="person__last">WELTAK</span></p>
    <p class="person__role">Fitoterapeuta</p>
  </div>

  <div class="brand"><span class="brand__dot"></span>OSRODEK ZIELNIKA</div>

  <div class="contact">
    <p class="contact__row">
      <svg class="contact__icon" viewBox="0 0 10 10" aria-hidden="true"><path d="M2 0.5 L3.6 2.6 L2.7 3.7 C3.3 5 4.6 6.4 6 7 L7.2 6.1 L9.5 7.7 L8.4 9.5 C4.3 9.3 0.6 5.6 0.5 1.6 Z"/></svg>
      574 806 215
    </p>
    <p class="contact__row">
      <svg class="contact__icon" viewBox="0 0 10 10" aria-hidden="true"><path d="M0 2 H10 V8.5 H0 Z M0.8 2.6 L5 5.6 L9.2 2.6" stroke="#fff" stroke-width="0.8"/></svg>
      piotrweltak@osrodekzielnika.com
    </p>
  </div>
  <p class="address">Dąbrowa Sękowska 14 ,<br>38-415 Mielnik</p>

  <svg class="base-bands" width="440" height="20" viewBox="0 0 440 20" aria-hidden="true">
    <polygon points="0,6 218,6 211,20 0,20" fill="var(--bark)"/>
    <polygon points="223,0 440,0 440,20 207,20" fill="var(--leaf)"/>
  </svg>
</section>

<section class="card card--back" aria-label="Back of business card">
  <div class="brand"><span class="brand__dot"></span>OSRODEK ZIELNIKA</div>
  <ul class="services services--left">
    <li>Lyme disease</li>
    <li>Autism</li>
    <li>Autoimmune diseases</li>
  </ul>
  <ul class="services services--right">
    <li>Herbs with science</li>
    <li>Immunologu</li>
    <li>Pharmacology</li>
  </ul>
</section>

</body>
</html>
```